Anzeigengestaltung für Stellenanzeige
Zielgruppe
Wir sind ein Abrechnungsunternehmen das für Zahnärzte die zahnmedizinische und zahntechnische Abrechnung von extern übernimmt.
Aufgrund einer Erweiterung suchen wir neues Personal welches uns unterstützt. Deshalb benötigen wir einen Stellenanzeige.
Wir suchen Personal - zahnmedizinische Fachangestellte mit Erfahrung in der Abrechnung
Abkürzungen: ZFA oder ZMV beides gewünscht wenn Abrechnungskenntnisse vorhanden sind.
Aufgabenstellung
Bitte Stellenanzeige unserer Website anpassen, www.zahnkanzleimerwen.de
logo bitte con Website übernehmen.
Moderne Gestaltung
Wir bieten:
-Anstellung Teilzeit oder Vollzeit
-Ein motiviertes und kompetentes Team
-Fort- und Weitermöglichkeiten
-Flexible Arbeits- und Urlaubszeiten
-Attraktive leistungsgerechte Bezahlung
Ihr Profil
Um die Stelle gut ausfüllen zu können, wünschen wir uns von Ihnen:
Abgeschlossene Ausbildung zum/zur Zahnmedizinische Fachangestellte, Zahnmedizinische Verwaltungsfachangestellte (m/w/d)
Selbstständiges Arbeiten und Einsatzbereitschaft
Gute PC-Kenntnisse und sicherer Umgang mit gängigen Office-Anwendungen
Erfahrung in der zahmedizinischen Abrechnung
Sorgfalt, Teamfähigkeit
Engagement und Freude am Beruf
Wir haben Ihr Interesse geweckt dann senden Sie uns Ihre Bewerbung an: t.brellmann@zahnkanzleimerwen.de
------Beispiel----------
Gerne auch eigene Beispiele....

```html
<!DOCTYPE html>
<html lang="de">
<head>
<meta charset="utf-8">
<title>Stellenanzeige – Zahnkanzlei Merwen</title>
<link href="https://fonts.googleapis.com/css2?family=Jost:wght@300;400;500;600&display=swap" rel="stylesheet">
<style>
  :root {
    --bg-deep: #141414;
    --bg-mid: #262626;
    --bg-light: #333231;
    --text-soft: #ddd5cb;
    --heading: #c7bdb1;
    --accent-white: #ffffff;
    --photo-dark: #2a2622;
    --photo-warm: #b9a58f;
  }
  * { margin: 0; padding: 0; box-sizing: border-box; }
  html, body { width: 859px; height: 1200px; overflow: hidden; background: var(--bg-deep); }
  .ad {
    position: relative;
    width: 859px;
    height: 1200px;
    overflow: hidden;
    font-family: "Jost", sans-serif;
    color: var(--text-soft);
    background:
      radial-gradient(ellipse at 30% 20%, var(--bg-light) 0%, transparent 55%),
      radial-gradient(ellipse at 85% 75%, #2c2c2b 0%, transparent 50%),
      linear-gradient(160deg, var(--bg-mid) 0%, #1c1c1c 55%, var(--bg-deep) 100%);
  }
  .brand {
    position: absolute;
    top: 96px;
    left: 495px;
    width: 322px;
    text-align: center;
  }
  .brand-name {
    font-weight: 500;
    font-size: 31px;
    letter-spacing: -0.5px;
    color: var(--heading);
    line-height: 40px;
  }
  .brand-tagline {
    margin-top: 10px;
    font-weight: 400;
    font-size: 10.5px;
    letter-spacing: 2.2px;
    color: var(--heading);
  }
  .headline {
    position: absolute;
    top: 222px;
    left: 0;
    width: 859px;
    text-align: center;
    font-weight: 600;
    font-size: 33px;
    letter-spacing: 0.3px;
    color: var(--heading);
  }
  .copy {
    position: absolute;
    left: 0;
    width: 859px;
    text-align: center;
    font-weight: 300;
    font-size: 20.5px;
    line-height: 28.6px;
  }
  .intro { top: 306px; }
  .section-title {
    font-weight: 600;
    font-size: 20px;
    color: var(--heading);
    letter-spacing: 0.3px;
  }
  .offer { top: 420px; }
  .profile { top: 620px; }
  .photo {
    position: absolute;
    left: 30px;
    top: 918px;
    width: 300px;
    height: 282px;
    background: radial-gradient(ellipse at 50% 55%, var(--photo-warm) 0%, #7a6a5a 35%, var(--photo-dark) 70%, transparent 100%);
    opacity: 0.85;
  }
  .contact {
    position: absolute;
    left: 390px;
    top: 1002px;
    width: 416px;
    text-align: center;
  }
  .contact-title {
    font-weight: 600;
    font-size: 21px;
    line-height: 28px;
    color: var(--heading);
  }
  .contact-note {
    margin-top: 32px;
    font-weight: 300;
    font-size: 20px;
    line-height: 28px;
  }
  .contact-mail {
    font-weight: 600;
    font-size: 19px;
    line-height: 28px;
    color: var(--accent-white);
  }
</style>
</head>
<body>
<main class="ad">
  <header class="brand">
    <div class="brand-name">Zahnkanzlei Merwen</div>
    <div class="brand-tagline">Zahnärztliche Abrechnung &amp; Management</div>
  </header>

  <h1 class="headline">WIR SUCHEN PERSONAL!</h1>

  <p class="copy intro">
    Zahnmedizinische Fachangestellte mit Erfahrung in der Abrechnung<br>
    Abkürzung: ZFA oder ZMV beides gewünscht, wenn<br>
    Abrechnungskenntnisse vorhanden sind
  </p>

  <section class="copy offer">
    <h2 class="section-title">WIR BIETEN:</h2>
    • Anstellung Teilzeit oder Vollzeit<br>
    • Ein motiviertes und kompetentes Team<br>
    • Fort- und Weitermöglichkeiten<br>
    • Flexible Arbeits- und Urlaubszeiten<br>
    • Attraktive leistungsgerechte Bezahlung
  </section>

  <section class="copy profile">
    <h2 class="section-title">IHR PROFIL:</h2>
    Um die Stelle gut ausfüllen zu können, wünschen wir uns von Ihnen:<br>
    • Abgeschlossene Ausbildung zum/zur Zahnmedizinische Fachangestellte,<br>
    Zahnmedizinische Verwaltungsfachangestellte (m/w/d)<br>
    • Selbstständiges Arbeiten und Einsatzbereitschaft<br>
    • Gute PC-Kenntnisse und sicherer Umgang mit gängigen<br>
    Office-Anwendungen<br>
    • Erfahrung in der zahmedizinischen Abrechnung<br>
    • Sorgfalt, Teamfähigkeit<br>
    • Engagement und Freude am Beruf
  </section>

  <div class="photo" role="img" aria-label="Foto von zwei Mitarbeiterinnen in beigen Blazern"></div>

  <aside class="contact">
    <h2 class="contact-title">WIR HABEN IHR INTERESSE<br>GEWECKT?!</h2>
    <p class="contact-note">Dann senden Sie uns Ihre Bewerbung an:</p>
    <p class="contact-mail">t.brellmann@zahnkanzleimerwen.de</p>
  </aside>
</main>
</body>
</html>
```